Nexor Turbo Business Card Design

This is a start up company that has state of the art patented technology for turbo chargers,that can be used on engines, gas or diesel, for any type of automotive,aviation,marine or industrial purpose.
This technology will provide longer life,lower maintenance and better performance and help produce lower emissions with any turbocharged engine.Red would be a predominate color and the design should communicate the latest technology,economy and
Environmental concern.
This product will initially be distributed in the U.S.A. But should move rapidly to global use.
Updates

Thank you for your design submissions, I have increased the budget for this job because my initial order was too low for the quality of work shown, plus I would Like to see some more options. I have a meeting this Sunday with my other partners and would anticipate being able to give you some feedback by the Beginning of next week. Regards.

Thank you for everyone's participation. The deadline is still open until 6/15 and my partners and I have a meeting Scheduled this weekend. At this time we have not ruled anyone out, But will be making a decision during the course of our meeting and wil Decide which direction we will be going in by the beginning of the week. Thanks again, regards, Dan Ferris.

Hello everybody, Sorry for the delay in communication, we have been very busy in putting the start up together. We are still not decided on the design of the business card and have a wide range to choose from. I would anticipated we shall have an answer within the next two weeks. Regards, Dan Ferris.

Target Market(s)

Manufacturers and wholesalers' of OEM and replacement turbochargers

Industry/Entity Type

Industrial

Contact Information for Business Card

We need a logo that should incorporate the " Nexor, a " possibly super imposed over a turbo charger with the fan blades of the turbocharger showing in the center of the "a" .
Name,title,phone number and email address only, no street/mailing address at this time.
The full name of the company is
" Nexor Turbo Technologies LLC "
For the initial card you can use my info.
Daniel Ferris
VP Sales & Marketing
dferris@nexorturbotechnologies.com
555 014 2876

Requirements
Must have
• The Nexor A, the outline of a turbo charger
Nice to have
• Something classy and simple and worldly (global)
Should not have
• No engines,cars,boats,planes

```html
<!DOCTYPE html>
<html lang="en">
<head>
<meta charset="utf-8">
<title>Nexor Turbo Technologies LLC – Business Card</title>
<link href="https://fonts.googleapis.com/css2?family=Arimo:wght@400;700&display=swap" rel="stylesheet">
<style>
  :root {
    --brand-red: #e01f26;
    --card-white: #ffffff;
    --backdrop: #ecebe8;
    --text-light: #ffffff;
  }
  * { margin: 0; padding: 0; box-sizing: border-box; }
  html, body {
    width: 1200px;
    height: 831px;
    overflow: hidden;
    background: var(--backdrop);
    font-family: "Arimo", Arial, sans-serif;
  }
  .business-card {
    position: absolute;
    left: 100px;
    top: 145px;
    width: 1000px;
    height: 540px;
    background: var(--card-white);
    box-shadow: 0 6px 22px rgba(0, 0, 0, 0.18);
    overflow: hidden;
  }
  .contact-panel {
    position: absolute;
    left: 497px;
    top: 0;
    right: 0;
    bottom: 0;
    background: var(--brand-red);
    color: var(--text-light);
    padding: 114px 0 0 50px;
  }
  .person-name {
    font-size: 46px;
    font-weight: 700;
    line-height: 1;
  }
  .person-title {
    font-size: 33px;
    font-weight: 400;
    line-height: 1.1;
    margin-top: 2px;
  }
  .person-phone {
    font-size: 33px;
    font-weight: 400;
    margin-top: 72px;
  }
  .brand-block {
    position: absolute;
    left: 84px;
    top: 140px;
    color: var(--brand-red);
    font-weight: 400;
  }
  .brand-mark {
    display: block;
    width: 96px;
    height: 96px;
    border-radius: 50%;
    background: var(--brand-red);
    margin: 0 0 30px 60px;
  }
  .brand-name {
    font-size: 42px;
    line-height: 1.05;
  }
  .brand-suffix {
    font-size: 31px;
    line-height: 1.1;
    padding-left: 20px;
  }
  .email-band {
    position: absolute;
    left: 14px;
    right: 0;
    bottom: 0;
    height: 54px;
    background: var(--brand-red);
    color: var(--text-light);
    font-size: 35px;
    line-height: 54px;
    padding-left: 62px;
  }
</style>
</head>
<body>
  <article class="business-card">
    <div class="brand-block">
      <span class="brand-mark" aria-hidden="true"></span>
      <p class="brand-name">Nexor Turbo</p>
      <p class="brand-suffix">Technologies LLC</p>
    </div>
    <section class="contact-panel">
      <h1 class="person-name">Daniel Ferris</h1>
      <p class="person-title">VP Sales &amp; Marketing</p>
      <p class="person-phone">555 014 2876</p>
    </section>
    <footer class="email-band">dferris@nexorturbotechnologies.com</footer>
  </article>
</body>
</html>
```